Summit slim shape co

We want a yard sign designed people can read from inside their cars. 24"x18". We are a start up business in Minneapolis Mn. We are the FAT LOSS place. We guarantee 25-45+lbs. of fat loss in 40 days. Because of our technology. Its Doctor supervised for safety and results. WWW.summitslimshapeCo.com

Industry/Entity Type

Business

```html
<!DOCTYPE html>
<html lang="en">
<head>
<meta charset="utf-8">
<title>Summit Slim Shape Co – Fat Loss Yard Sign</title>
<link rel="stylesheet" href="https://fonts.googleapis.com/css2?family=Ultra&family=Alfa+Slab+One&family=Oxygen:wght@300;400&family=Open+Sans:wght@700&family=PT+Sans+Narrow:wght@700&display=block">
<style>
  :root {
    --green: #8dc63f;
    --white: #ffffff;
    --black: #000000;
    --purple: #6b3a8c;
    --red: #be1e2d;
    --orange: #f7941d;
    --display: "Ultra", "Alfa Slab One", "Rockwell Extra Bold", serif;
  }
  * { margin: 0; padding: 0; box-sizing: border-box; }
  html, body { width: 848px; height: 1200px; overflow: hidden; background: var(--white); }
  .canvas { position: relative; width: 848px; height: 1200px; background: var(--white); }
  .sign { position: absolute; left: 21px; top: 64px; width: 804px; height: 1072px; overflow: hidden; background: var(--white); }
  .layer { position: absolute; left: 0; top: 0; }
  .figure { position: absolute; left: 6px; top: 135px; width: 360px; height: 770px; }
  .display { font-family: var(--display); }
  .headline, .lose, .days { fill: var(--black); }
  .amount { fill: var(--purple); }
  .guarantee-word { fill: var(--red); }
  .in { font-family: "Oxygen", sans-serif; font-size: 27px; fill: var(--black); }
  .cta-label { font-family: "Open Sans", sans-serif; font-weight: 700; font-size: 45px; fill: var(--white); }
  .phone { font-family: "PT Sans Narrow", sans-serif; font-weight: 700; font-size: 78px; fill: var(--black); }
  .tech-bar { position: absolute; left: 288px; top: 728px; width: 516px; height: 45px; background: var(--black); color: var(--white); font-family: "Oxygen", sans-serif; font-size: 29px; display: flex; align-items: center; justify-content: center; }
  .supervised { position: absolute; right: 58px; top: 792px; font-family: "Oxygen", sans-serif; font-size: 28px; color: var(--black); text-align: right; line-height: 1.3; white-space: nowrap; }
  .web-band { position: absolute; left: 0; top: 987px; width: 804px; height: 85px; background: var(--purple); color: var(--white); font-family: "Oxygen", sans-serif; font-weight: 300; font-size: 46px; display: flex; align-items: center; justify-content: center; white-space: nowrap; }
</style>
</head>
<body>
<div class="canvas">
  <div class="sign">
    <svg class="layer" width="804" height="1072" viewBox="0 0 804 1072">
      <path d="M0,0 H804 V181 C540,196 160,356 0,682 Z" fill="var(--green)"/>
    </svg>

    <svg class="figure" role="img" aria-label="Illustration of a slim woman in a green top and purple capris holding an apple, wrapped in a measuring tape" viewBox="0 0 360 770">
      <defs>
        <linearGradient id="figureTone" x1="0" y1="0" x2="0" y2="1">
          <stop offset="0" stop-color="#f6b13a"/>
          <stop offset="0.3" stop-color="#a9d64a"/>
          <stop offset="0.65" stop-color="#8a4fa8"/>
          <stop offset="1" stop-color="#f0b27a"/>
        </linearGradient>
      </defs>
      <rect x="0" y="0" width="360" height="770" rx="40" fill="url(#figureTone)" opacity="0.5"/>
    </svg>

    <svg class="layer" width="804" height="1072" viewBox="0 0 804 1072">
      <text class="display headline" x="83" y="126" font-size="124" textLength="634" lengthAdjust="spacingAndGlyphs">FAT LOSS</text>

      <g transform="translate(390 364) rotate(-19)">
        <text class="display guarantee-word" x="0" y="0" font-size="56" textLength="412" lengthAdjust="spacingAndGlyphs">GUARANTEED!</text>
        <path d="M40,14 L414,8 L412,20 L60,24 L30,34 Z" fill="var(--red)"/>
      </g>

      <text class="display lose" x="376" y="526" font-size="116" textLength="305" lengthAdjust="spacingAndGlyphs">LOSE</text>
      <text class="display amount" x="295" y="614" font-size="100" textLength="464" lengthAdjust="spacingAndGlyphs">25-45+lbs.</text>
      <text class="in" x="316" y="661">in</text>
      <text class="display days" x="352" y="695" font-size="100" textLength="352" lengthAdjust="spacingAndGlyphs">40 days</text>

      <path d="M0,928 H328 V917 L394,957 L328,997 V987 H0 Z" fill="var(--orange)"/>
      <text class="cta-label" x="51" y="974" textLength="263" lengthAdjust="spacingAndGlyphs">START NOW!</text>
      <text class="phone" x="405" y="968" textLength="378" lengthAdjust="spacingAndGlyphs">612-555-0148</text>
    </svg>

    <div class="tech-bar">Because of our technology</div>
    <p class="supervised">Doctor supervised<br>for safety and results</p>
    <div class="web-band">WWW.summitslimshapeCo.com</div>
  </div>
</div>
</body>
</html>
```